HOME PAGE AND AND SECONDARY DESIGN FOR INTERNAL PAGES

Construction company looking for an easy to navagate professional serious greyscale website with a good clean feel simple clean menu and responsive friendly design. Our main clientele is commercial properties business owners and investors of rental properties. This website is going to be static HTML5 and would need multiple sizing files for clean fast rendering. Clean and accurate design files a must so if your experienced awesome modern greyscale designer let's get started I need this done as soon as possible.

Industry/Entity Type

construction, electrical, plumbing, commercial build outs

Number of Pages Required

2 page

Font styles to use
Sans Serif

Colors

Designer to choose only greyscale colors for use in the design.

Requirements
Must have
• Main Menu... Home, Services, Projects, About our team

```html
<!DOCTYPE html>
<html lang="en">
<head>
<meta charset="utf-8">
<title>Stonegate Builders — Home</title>
<link rel="stylesheet" href="https://fonts.googleapis.com/css2?family=Montserrat:ital,wght@0,300;0,400;0,500;0,600;1,300;1,400&family=Bebas+Neue&family=Oswald:wght@200&display=swap">
<style>
:root{
  --ink:#1e1e1e;
  --text:#3a3a3a;
  --muted:#8a8a8a;
  --band:#e6e6e6;
  --card:#f1f1f1;
  --white:#ffffff;
  --footer:#333333;
  --footer-text:#d8d8d8;
}
*{margin:0;padding:0;box-sizing:border-box}
html,body{width:1200px;height:3291px;overflow:hidden;background:var(--white)}
body{position:relative;font-family:'Montserrat',sans-serif;color:var(--text)}
.abs{position:absolute}

/* header */
.site-header{left:0;top:0;width:1200px;height:123px;background:var(--white)}
.brand{left:215px;top:56px;display:flex;align-items:center;gap:8px;font-weight:600;font-size:14px;letter-spacing:1px;color:#555;white-space:nowrap}
.brand-mark{width:12px;height:12px;background:#555}
.main-nav{left:464px;top:58px;font-size:15px;font-weight:500;color:#444;letter-spacing:.3px}
.main-nav span{position:absolute;white-space:nowrap}

/* hero */
.hero{left:0;top:123px;width:1200px;height:552px;background:radial-gradient(ellipse at 60% 40%,#8a8a8a 0%,#4a4a4a 45%,#151515 100%)}
.hero-title{left:0;top:356px;width:1210px;text-align:center;font-family:'Bebas Neue',sans-serif;font-size:96px;color:var(--white);letter-spacing:-1px;line-height:1}
.hero-sub{left:0;top:448px;width:1200px;text-align:center;font-family:'Oswald',sans-serif;font-weight:200;font-size:36px;line-height:1;color:#ddd}
.hero-dots{left:531px;top:628px;display:flex;gap:23px}
.hero-dots i{display:block;width:17px;height:3px;background:#777}
.hero-dots i:first-child{background:var(--white)}

/* features */
.features{left:0;top:675px;width:1200px;height:292px;background:var(--band)}
.feature{top:675px;width:292px;height:292px;background:var(--card);box-shadow:0 2px 5px rgba(0,0,0,.35);text-align:center}
.feature svg{margin-top:27px}
.feature h3{font-weight:400;font-size:22px;color:#444;margin-top:14px}
.feature p{font-size:16px;line-height:19.5px;color:var(--muted);margin:18px 32px 0}

/* about */
.about-kicker{left:168px;top:1082px;font-style:italic;font-weight:300;font-size:22px;color:#444}
.about-title{left:168px;top:1108px;font-weight:400;font-size:30px;color:var(--ink)}
.about-text{left:164px;top:1160px;width:470px;font-size:18px;line-height:21px;letter-spacing:.6px;color:#555}
.btn{left:162px;top:1346px;width:148px;height:38px;border-radius:19px;background:var(--ink);color:var(--white);font-size:16px;font-weight:500;display:flex;align-items:center;justify-content:center}
.about-art{left:640px;top:975px;width:510px;height:500px;background:radial-gradient(circle at 50% 50%,#ececec,#ffffff 70%)}

/* stats */
.stats{left:0;top:1520px;width:1200px;height:269px;background:var(--band)}
.stat{top:1588px;width:260px;text-align:center;color:var(--ink)}
.stat strong{display:block;font-weight:500;font-size:50px;line-height:1;margin-top:6px}
.stat span{display:block;font-size:14px;font-weight:500;margin-top:2px}

/* services */
.svc-kicker{left:168px;top:1832px;font-style:italic;font-weight:300;font-size:22px;color:#444}
.svc-title{left:168px;top:1858px;font-size:30px;color:var(--ink)}
.svc-card{width:268px;height:267px;color:var(--white);overflow:hidden}
.svc-card .photo{position:absolute;inset:0}
.svc-card h4{position:absolute;left:15px;top:183px;font-size:15px;font-weight:500}
.svc-card p{position:absolute;left:14px;top:203px;right:16px;font-size:8.5px;line-height:10.5px;font-style:italic;font-weight:300;color:#ccc}

/* partners */
.divider{left:0;top:2553px;width:1200px;height:1px;background:#d0d0d0}
.partner{top:2720px;width:260px;text-align:center;font-weight:600;font-size:15px;letter-spacing:1px;white-space:nowrap}

/* footer */
.site-footer{left:0;top:2892px;width:1200px;height:399px;background:var(--footer);color:var(--footer-text)}
.f-head{font-size:18px;font-weight:500;color:var(--white)}
.f-text{font-size:13px;line-height:16px}
.f-links{font-size:13px;font-weight:500;line-height:22.5px;color:var(--white)}
.social{width:24px;height:24px;border:1px solid #bbb;display:flex;align-items:center;justify-content:center}
.newsletter{left:747px;top:3071px;width:240px;height:28px;background:var(--white);border:1px solid #ccc;font-size:12px;color:#aaa;padding:6px 8px}
.submit{position:absolute;right:10px;top:7px;width:54px;height:13px;border-radius:7px;background:#333;color:#fff;font-size:7px;text-align:center;line-height:13px}
.copyright{left:162px;top:3256px;font-size:13px}
.f-nav span{position:absolute;font-size:13px;white-space:nowrap}
</style>
</head>
<body>

<header class="abs site-header">
  <div class="abs brand"><span class="brand-mark"></span>STONEGATE BUILDERS</div>
  <nav class="abs main-nav" aria-label="Main menu">
    <span style="left:0">HOME</span>
    <span style="left:101px">SERVICES ˅</span>
    <span style="left:225px">PROJECTS ˅</span>
    <span style="left:354px">ABOUT OUR TEAM</span>
  </nav>
</header>

<section class="abs hero" role="img" aria-label="Black and white photo of a construction worker in a hard hat cutting timber with a circular saw"></section>
<div class="abs hero-title">WE BUILD YOUR FANTASY</div>
<div class="abs hero-sub">Professional</div>
<svg class="abs" style="left:50px;top:370px" width="36" height="56" viewBox="0 0 36 56"><path d="M30 4 L8 28 L30 52" fill="none" stroke="#fff" stroke-width="8"/></svg>
<svg class="abs" style="left:1114px;top:370px" width="36" height="56" viewBox="0 0 36 56"><path d="M6 4 L28 28 L6 52" fill="none" stroke="#fff" stroke-width="8"/></svg>
<div class="abs hero-dots"><i></i><i></i><i></i><i></i></div>

<section class="abs features"></section>
<div class="abs feature" style="left:162px">
  <svg width="62" height="62" viewBox="0 0 62 62" fill="none" stroke="#222" stroke-width="2.5"><path d="M31 3l6 5 8-1 3 7 7 4-1 8 5 6-5 6 1 8-7 4-3 7-8-1-6 5-6-5-8 1-3-7-7-4 1-8-5-6 5-6-1-8 7-4 3-7 8 1z"/><circle cx="31" cy="31" r="15"/><path d="M24 31l5 5 9-10"/></svg>
  <h3>Quality Work</h3>
  <p>Lorem ipsum dolor sit amet, consectetuer adipiscing elit, sed diam nonummy nibh euismod tincidunt ut laoreet dolore</p>
</div>
<div class="abs feature" style="left:454px;background:#e8e8e8">
  <svg width="62" height="62" viewBox="0 0 62 62" fill="none" stroke="#222" stroke-width="2.5"><circle cx="31" cy="31" r="27"/><path d="M23 24a8 8 0 1 1 12 7c-3 2-4 3-4 7"/><circle cx="31" cy="45" r="1.5" fill="#222"/></svg>
  <h3>What We Do?</h3>
  <p>Lorem ipsum dolor sit amet, consectetuer adipiscing elit, sed diam nonummy nibh euismod tincidunt ut laoreet dolore</p>
</div>
<div class="abs feature" style="left:746px">
  <svg width="62" height="62" viewBox="0 0 62 62" fill="none" stroke="#222" stroke-width="2.5"><path d="M22 4l2 5M31 2v6M40 4l-2 5"/><path d="M8 42l16-20 8 6 10-6 14 18-16 14-12-6z"/><path d="M24 34l6 6M30 30l8 8M36 28l8 8"/></svg>
  <h3>24/7 Support</h3>
  <p>Lorem ipsum dolor sit amet, consectetuer adipiscing elit, sed diam nonummy nibh euismod tincidunt ut laoreet dolore</p>
</div>

<div class="abs about-kicker">About Us</div>
<h2 class="abs about-title">We build your fantasy</h2>
<p class="abs about-text">Lorem Ipsum is simply dummy text of the printing and typesetting industry. Lorem Ipsum has been the industry's standard dummy text ever since the 1500s, when an unknown printer took a galley of type and scrambled it to make a type specimen book. It has survived not only five centuries, but also the leap into electronic typesetting, remaining essentially unchanged.</p>
<div class="abs btn">LEARN MORE</div>
<div class="abs about-art" role="img" aria-label="Line sketch of a building frame with columns and floor slabs"></div>

<section class="abs stats"></section>
<div class="abs stat" style="left:160px">
  <svg width="66" height="62" viewBox="0 0 66 62" fill="none" stroke="#111" stroke-width="2.5"><path d="M24 14a9 9 0 0 1 18 0z"/><circle cx="33" cy="22" r="7"/><path d="M20 60V42a13 13 0 0 1 26 0v18"/><path d="M4 28a7 7 0 0 1 14 0zM48 28a7 7 0 0 1 14 0z"/><circle cx="11" cy="35" r="5"/><circle cx="55" cy="35" r="5"/><path d="M2 60V50a9 9 0 0 1 16-5M64 60V50a9 9 0 0 0-16-5"/></svg>
  <strong>250+</strong><span>EXPERT WORKERS</span>
</div>
<div class="abs stat" style="left:465px">
  <svg width="66" height="62" viewBox="0 0 66 62" fill="none" stroke="#111" stroke-width="2.5"><path d="M8 38L33 16l25 22M14 33v26h38V33"/><path d="M10 10l44 44M54 10L10 54"/><path d="M26 50h14v9H26z"/></svg>
  <strong>500+</strong><span>COMPLETED PROJECTS</span>
</div>
<div class="abs stat" style="left:770px">
  <svg width="66" height="62" viewBox="0 0 66 62" fill="none" stroke="#111" stroke-width="2.5"><path d="M6 6h58M14 6v54M54 6v14"/><path d="M22 20h26v40H22z"/><path d="M28 28h5v5h-5zM37 28h5v5h-5zM28 38h5v5h-5zM37 38h5v5h-5z"/><path d="M4 60h60"/></svg>
  <strong>400+</strong><span>RUNNING PROJECTS</span>
</div>

<div class="abs svc-kicker">Our Services</div>
<h2 class="abs svc-title" style="font-weight:400">We provide best services</h2>

<div class="abs svc-card" style="left:164px;top:1932px">
  <div class="photo" role="img" aria-label="Architect sketching building plans on paper" style="background:linear-gradient(180deg,#8c8c8c,#5e5e5e 55%,#222)"></div>
  <h4>ARCHITECTURE</h4><p>Lorem ipsum dolor sit amet, consectetuer adipiscing elit, sed diam nonummy nibh euismod tincidunt ut laoreet dolore magna aliquam erat volutpat. Ut wisi enim ad minim veniam, quis nostrud exerci tation</p>
</div>
<div class="abs svc-card" style="left:466px;top:1932px">
  <div class="photo" role="img" aria-label="Polished metal plumbing pipes and valves" style="background:linear-gradient(180deg,#a0a6aa,#5a6064 55%,#1f2224)"></div>
  <h4>PLUMBING</h4><p>Lorem ipsum dolor sit amet, consectetuer adipiscing elit, sed diam nonummy nibh euismod tincidunt ut laoreet dolore magna aliquam erat volutpat. Ut wisi enim ad minim veniam, quis nostrud exerci tation</p>
</div>
<div class="abs svc-card" style="left:767px;top:1932px">
  <div class="photo" role="img" aria-label="Electrician in a hard hat working on overhead power lines" style="background:linear-gradient(180deg,#7f8a78,#4d5548 55%,#1e201c)"></div>
  <h4>ELECTRICAL</h4><p>Lorem ipsum dolor sit amet, consectetuer adipiscing elit, sed diam nonummy nibh euismod tincidunt ut laoreet dolore magna aliquam erat volutpat. Ut wisi enim ad minim veniam, quis nostrud exerci tation</p>
</div>
<div class="abs svc-card" style="left:164px;top:2234px">
  <div class="photo" role="img" aria-label="Builder on timber wall framing under a blue sky" style="background:linear-gradient(180deg,#4d86a8,#6f7c82 50%,#2a2522)"></div>
  <h4>COMMERCIAL BUILD OUTS</h4><p>Lorem ipsum dolor sit amet, consectetuer adipiscing elit, sed diam nonummy nibh euismod tincidunt ut laoreet dolore magna aliquam erat volutpat. Ut wisi enim ad minim veniam, quis nostrud exerci tation</p>
</div>
<div class="abs svc-card" style="left:466px;top:2234px">
  <div class="photo" role="img" aria-label="Tower crane lifting a load above a building site" style="background:linear-gradient(180deg,#b9c0c6,#8c8f92 50%,#2a2a2a)"></div>
  <h4>CONSTRUCTION</h4><p>Lorem ipsum dolor sit amet, consectetuer adipiscing elit, sed diam nonummy nibh euismod tincidunt ut laoreet dolore magna aliquam erat volutpat. Ut wisi enim ad minim veniam, quis nostrud exerci tation</p>
</div>
<div class="abs svc-card" style="left:767px;top:2234px">
  <div class="photo" role="img" aria-label="Painter rolling paint onto an interior wall" style="background:linear-gradient(180deg,#a6a29c,#6e6a66 55%,#222)"></div>
  <h4>PAINTING</h4><p>Lorem ipsum dolor sit amet, consectetuer adipiscing elit, sed diam nonummy nibh euismod tincidunt ut laoreet dolore magna aliquam erat volutpat. Ut wisi enim ad minim veniam, quis nostrud exerci tation</p>
</div>

<div class="abs divider"></div>
<div class="abs partner" style="left:108px;color:#9a9a9a">STONEGATE BUILDERS</div>
<div class="abs partner" style="left:349px;color:#707070">STONEGATE BUILDERS</div>
<div class="abs partner" style="left:591px;color:#474747">STONEGATE BUILDERS</div>
<div class="abs partner" style="left:832px;color:#111">STONEGATE BUILDERS</div>

<footer class="abs site-footer"></footer>
<div class="abs f-head" style="left:164px;top:2960px">Office</div>
<div class="abs f-text" style="left:164px;top:3006px;color:var(--footer-text)">48 Quarry Lane, Granite Falls, 55012<br>United States of America</div>
<div class="abs f-text" style="left:164px;top:3050px;color:var(--footer-text)">Phone: <b style="color:#fff;font-weight:500">+1 555 014 2290</b></div>
<div class="abs f-text" style="left:164px;top:3072px;color:var(--footer-text)">Email: <b style="color:#fff;font-weight:500">hello@stonegatebuilders.com</b></div>
<div class="abs social" style="left:163px;top:3114px"><svg width="10" height="10"><rect width="10" height="10" fill="none" stroke="#ccc"/></svg></div>
<div class="abs social" style="left:215px;top:3114px"><svg width="10" height="10"><rect width="10" height="10" fill="none" stroke="#ccc"/></svg></div>
<div class="abs social" style="left:266px;top:3114px"><svg width="10" height="10"><rect width="10" height="10" fill="none" stroke="#ccc"/></svg></div>
<div class="abs social" style="left:318px;top:3114px"><svg width="10" height="10"><rect width="10" height="10" fill="none" stroke="#ccc"/></svg></div>

<div class="abs f-head" style="left:454px;top:2960px">Services</div>
<div class="abs f-links" style="left:454px;top:2999px">Architecture<br>Plumbing<br>Electrical<br>Commerical Build Outs<br>Construction<br>Painting</div>

<div class="abs f-head" style="left:746px;top:2960px">Newsletter</div>
<div class="abs f-text" style="left:747px;top:3006px;color:var(--footer-text)">Sign up today for hints, tips &amp; the<br>latest product news</div>
<div class="abs newsletter">Email address here<span class="submit">SUBMIT</span></div>

<div class="abs copyright" style="color:var(--footer-text)">Copyright © 2023 <b style="color:#fff;font-weight:500">Stonegate Builders</b>, All Right Reserved.</div>
<div class="abs f-nav" style="left:0;top:3256px;color:var(--footer-text)">
  <span style="left:618px">HOME</span>
  <span style="left:703px">SERVICES</span>
  <span style="left:815px">PROJECTS</span>
  <span style="left:915px">ABOUT OUR TEAM</span>
</div>

</body>
</html>
```